Tarnwick is a steel frame construction company that builds residential and commercial homes

1. Homepage (we are after a basic website)
Hero Section:
A full-width image or video showcasing steel frames in construction or a finished project.
Tagline: Short, impactful tagline (e.g., "Strong Structures for Tomorrow").
Call-to-Action (CTA): A prominent "Get a Quote" or "Contact Us" button.
About Us (Snapshot Section):

A few lines about the company, emphasizing experience, certifications, and commitment to quality.
Include a "Learn More" button linking to the detailed About Us page.
Products/Services Section:

Feature the main products like steel frames for industrial, residential, and commercial projects.
Each category should have a "Learn More" link to a dedicated product page.
Project Showcase/Portfolio:

Display 2-3 featured projects with images, descriptions, and a "View All Projects" button.
Certifications & Partners:

Display logos of certifications (QSB, local building standards) and partnerships with construction companies or industry bodies.
Footer:

Contact information, quick links (Home, About, Products, Services, Contact), and social media icons.
2. Products Page
Overview:

A grid or list layout showing different steel frame products or services.
Each product should have a title, brief description, and a thumbnail image.
Individual Product Pages:

Detailed information on specific products (e.g., “Steel Frames for Residential Construction”):
Features: Highlight specific features like durability, eco-friendliness, precision, etc.
Technical Specs: Material grades, dimensions, finishes available.
Case Studies: A couple of client testimonials or case studies of where this product was used.
Downloadable Resources:

Technical datasheets or catalogs for users to download.
Include a form to capture user information before they download the document (optional for lead generation).
3. Projects/Portfolio Page
Gallery of Projects:
Display completed projects with high-quality images, each linked to a project detail page.
Filter options (e.g., industrial, residential, commercial).
Project Detail Pages:
A detailed description of the project, challenges, and how the steel frames were used.
other website we liked are:
https://www.tarnwickbuilds.example/
https://orlenbayhomes.example/

1. Objective:
Create an informative, professional, and visually appealing website that promotes steel frame construction solutions, showcasing the company’s offerings, expertise, and projects.
The website should highlight the benefits of steel frames (e.g., durability, sustainability, and cost-efficiency) and cater to both B2B and B2C clients.
2. Target Audience:
Primary: Architects, builders, and construction companies.
Secondary: Homeowners, investors, and property developers looking for modern, durable construction solutions.

```html
<!DOCTYPE html>
<html lang="en">
<head>
<meta charset="utf-8">
<title>Tarnwick — Steel Frame Construction</title>
<link href="https://fonts.googleapis.com/css2?family=Poppins:wght@400;500;600;700&family=Roboto+Slab:wght@600;700&display=swap" rel="stylesheet">
<style>
:root{
  --blue:#1672c6;
  --blue-dark:#0d4f8f;
  --black:#000;
  --ink:#1b1b1b;
  --white:#fff;
  --line:#d9dfe6;
  --muted:#3a3a3a;
}
*{box-sizing:border-box;margin:0;padding:0}
html,body{width:1200px;height:4651px;overflow:hidden}
body{position:relative;font-family:'Poppins',sans-serif;color:var(--ink);background:var(--white)}
.abs{position:absolute}
section,header,footer,nav{position:absolute;left:0;width:1200px}
.serif{font-family:'Roboto Slab',serif}
.btn{position:absolute;display:flex;align-items:center;justify-content:center;background:var(--blue);color:var(--white);font-size:15px;font-weight:500;text-transform:uppercase;letter-spacing:.2px}
.sec-title{position:absolute;left:0;width:1200px;text-align:center;font-family:'Roboto Slab',serif;font-weight:700;font-size:36px;color:var(--blue);text-transform:uppercase}
.sec-title span{text-decoration:underline;text-decoration-thickness:3px;text-underline-offset:8px}
.sec-text{position:absolute;left:260px;width:680px;text-align:center;font-size:15px;line-height:24px}
.photo{position:absolute}

/* header */
.topbar{top:0;height:100px}
.brand{position:absolute;left:63px;top:30px;display:flex;align-items:center;gap:10px}
.brand-square{width:34px;height:34px;background:var(--blue)}
.brand-name{font-weight:700;font-size:30px;color:var(--blue);letter-spacing:1px}
.contact-item{position:absolute;top:30px;display:flex;gap:14px;align-items:center}
.contact-item small{display:block;font-size:14px;color:#444}
.contact-item b{font-size:17px;font-weight:600}
.mainnav{top:100px;height:86px;background:var(--black)}
.mainnav ul{position:absolute;left:63px;top:32px;display:flex;gap:32px;list-style:none}
.mainnav li{color:var(--white);font-size:16px;font-weight:600}
.mainnav li.active{color:var(--blue)}

/* hero */
.hero{top:186px;height:603px}
.hero-photo{left:0;top:0;width:1200px;height:603px;background:linear-gradient(160deg,#3b4450 0%,#6a5a48 35%,#c9772c 60%,#e7a04a 72%,#3a3230 100%)}
.hero h1{position:absolute;left:63px;top:122px;font-family:'Roboto Slab',serif;font-weight:700;font-size:52px;line-height:70px;color:var(--white)}
.hero p{position:absolute;left:63px;top:345px;width:440px;font-size:15px;line-height:24px;color:var(--white)}

/* about */
.about{top:789px;height:736px}
.about h2{position:absolute;left:660px;top:98px;font-family:'Roboto Slab',serif;font-size:36px;color:var(--blue)}
.about h2 span{text-decoration:underline;text-decoration-thickness:3px;text-underline-offset:8px}
.about .copy{position:absolute;left:660px;top:198px;width:425px;font-size:15px;line-height:24px}
.about .copy p+p{margin-top:4px}
.exp{position:absolute;left:660px;top:455px;display:flex;align-items:center;gap:18px}
.exp div{color:var(--blue);font-size:26px;line-height:27px}
.exp b{color:var(--ink);font-weight:500;font-size:34px}

/* products */
.products{top:1525px;height:697px;background:linear-gradient(180deg,#3e6f96 0%,#7597b2 30%,#35638d 70%,#1f4f7e 100%)}
.products .sec-title{color:var(--white)}
.products .sec-text{color:var(--white)}
.tab{position:absolute;top:183px;height:37px;display:flex;align-items:center;justify-content:center;background:var(--blue);color:var(--white);font-size:15px;border:2px solid var(--white)}
.tab.active{background:var(--white);color:var(--blue)}
.pcard{position:absolute;top:275px;width:321px;height:335px}
.pcard .label{position:absolute;left:0;bottom:0;width:100%;height:45px;background:var(--black);color:var(--white);font-size:18px;display:flex;align-items:center;gap:10px;padding-left:16px}
.pcard .label.light{background:var(--white);color:var(--blue)}

/* services */
.services{top:2222px;height:558px}
.scard{position:absolute;top:266px;width:349px;height:227px;border:2px solid var(--blue);text-align:center;padding-top:58px}
.scard h3{font-size:26px;font-weight:500;text-transform:uppercase}
.scard p{font-size:15px;line-height:24px;margin:6px auto 0;width:280px}
.scard .btn{left:95px;top:172px;width:157px;height:38px}
.scard.featured{background:var(--blue);color:var(--white)}
.scard.featured .btn{border:2px solid var(--white)}
.sicon{position:absolute;top:208px;width:100px;height:100px;border-radius:50%;display:flex;align-items:center;justify-content:center;background:var(--blue)}
.sicon.light{background:#eaeaea}

/* projects */
.projects{top:2780px;height:790px;background:linear-gradient(180deg,#4a6f95 0%,#1f4778 50%,#18385f 100%)}
.projects .sec-title{color:var(--white)}
.projects .sec-text{color:#d7e3f0}
.jcard{position:absolute;top:212px;width:349px;height:418px}
.jcard .img{position:absolute;left:0;top:0;width:100%;height:270px}
.jcard .body{position:absolute;left:0;top:270px;width:100%;height:148px;background:var(--black);color:var(--white);padding:16px 16px}
.jcard .body.blue{background:var(--blue)}
.jcard h4{font-size:18px;font-weight:500;line-height:27px;width:260px}
.jcard p{font-size:13px;line-height:20px;margin-top:8px}
.jcard svg.arr{position:absolute;right:16px;top:20px}

/* partners */
.partners{top:3570px;height:401px}
.pbox{position:absolute;top:198px;width:259px;height:157px;border:2px solid #bfc6cd;box-shadow:0 3px 6px rgba(0,0,0,.15);display:flex;align-items:center;justify-content:center}

/* certs + contact */
.split{top:3971px;height:434px}
.certs{position:absolute;left:63px;top:0;width:490px;height:434px;background:var(--black);color:var(--white)}
.certs h2,.contact h2{font-family:'Roboto Slab',serif;font-size:36px;font-weight:700;text-transform:uppercase}
.certs h2 span,.contact h2 span{text-decoration:underline;text-decoration-thickness:3px;text-underline-offset:8px}
.certs h2{position:absolute;left:57px;top:30px}
.certs p{position:absolute;left:57px;top:95px;width:340px;font-size:15px;line-height:24px}
.round{position:absolute;width:40px;height:40px;border-radius:50%;border:2px solid var(--white);display:flex;align-items:center;justify-content:center}
.dot{position:absolute;top:392px;width:20px;height:4px;background:var(--white)}
.contact{position:absolute;left:553px;top:0;width:584px;height:434px;background:var(--blue)}
.contact h2{position:absolute;left:0;width:100%;text-align:center;top:30px;color:var(--white)}
.field{position:absolute;background:var(--white);font-size:14px;color:#222;padding:12px 20px}
.submit{position:absolute;left:214px;top:352px;width:156px;height:38px;background:var(--black);color:var(--white);display:flex;align-items:center;justify-content:center;font-size:16px;font-weight:500}

/* footer */
.site-footer{top:4405px;height:246px;background:var(--black);color:var(--white)}
.foot-brand{position:absolute;left:63px;top:45px;width:274px;height:95px;background:#111;display:flex;align-items:center;justify-content:center;gap:10px}
.foot-brand b{font-size:32px;font-weight:700;color:var(--white);letter-spacing:1px}
.foot-brand i{width:30px;height:30px;background:var(--blue)}
.foot-links{position:absolute;left:355px;top:84px;display:flex;gap:32px;list-style:none}
.foot-links li{font-size:16px;font-weight:600}
.foot-links li.active{color:var(--blue)}
.social{position:absolute;top:78px;width:36px;height:36px;border-radius:50%;background:var(--blue)}
.foot-rule{position:absolute;left:0;top:180px;width:1200px;height:1px;background:#333}
.copyright{position:absolute;left:0;top:200px;width:1200px;text-align:center;font-size:14px}
</style>
</head>
<body>

<header class="topbar">
  <div class="brand"><span class="brand-square"></span><span class="brand-name">TARNWICK</span></div>
  <div class="contact-item" style="left:555px">
    <svg width="44" height="32" viewBox="0 0 44 32"><rect x="2" y="2" width="40" height="28" rx="2" fill="none" stroke="#1672c6" stroke-width="3"/><path d="M3 4l19 14 19-14" fill="none" stroke="#1672c6" stroke-width="3"/></svg>
    <div><small>MAIL</small><b>hello@tarnwick.example</b></div>
  </div>
  <div class="contact-item" style="left:970px">
    <svg width="40" height="40" viewBox="0 0 24 24"><path d="M6.6 10.8a15 15 0 006.6 6.6l2.2-2.2c.3-.3.7-.4 1-.2 1.1.4 2.3.6 3.6.6.6 0 1 .4 1 1V20c0 .6-.4 1-1 1A17 17 0 013 4c0-.6.4-1 1-1h3.5c.6 0 1 .4 1 1 0 1.3.2 2.5.6 3.6.1.3 0 .7-.2 1z" fill="none" stroke="#1672c6" stroke-width="1.6"/><path d="M14 3a7 7 0 017 7M14 6.5a3.5 3.5 0 013.5 3.5" fill="none" stroke="#1672c6" stroke-width="1.6"/></svg>
    <div><small>CALL</small><b>555 014 2318</b></div>
  </div>
</header>

<nav class="mainnav">
  <ul><li class="active">HOME</li><li>ABOUT</li><li>SERVICES</li><li>PRODUCTS</li><li>CONTACT</li></ul>
  <svg class="abs" style="left:892px;top:124px" width="36" height="36" viewBox="0 0 36 36"><circle cx="15" cy="15" r="11" fill="none" stroke="#fff" stroke-width="3"/><path d="M23 23l9 9" stroke="#fff" stroke-width="3"/></svg>
  <div class="btn" style="left:973px;top:24px;width:164px;height:38px">Get a Quote</div>
</nav>

<section class="hero">
  <div class="photo hero-photo" role="img" aria-label="Welder working on a steel frame at sunset"></div>
  <h1>Raising Standards<br>In Steel<br>Construction</h1>
  <p>Lorem ipsum odor amet, consectetuer adipiscing elit. Platea pulvinar lobortis fames, maecenas feugiat morbi venenatis.</p>
  <div class="btn" style="left:63px;top:439px;width:157px;height:40px">Contact Us</div>
  <svg class="abs" style="left:563px;top:264px" width="74" height="74" viewBox="0 0 74 74"><circle cx="37" cy="37" r="34" fill="#1672c6" stroke="#fff" stroke-width="4"/><path d="M29 24l22 13-22 13z" fill="#fff"/></svg>
</section>

<section class="about">
  <div class="abs" style="left:535px;top:136px;width:57px;height:350px;background:var(--blue)"></div>
  <div class="abs" style="left:115px;top:266px;width:133px;height:63px;background:var(--blue)"></div>
  <div class="abs" style="left:350px;top:447px;width:53px;height:168px;background:var(--blue)"></div>
  <div class="abs" style="left:196px;top:197px;width:52px;height:120px;border:1px solid #999;border-right:none"></div>
  <div class="photo" style="left:248px;top:97px;width:287px;height:350px;background:linear-gradient(180deg,#9aa4ad,#5d7c9f 60%,#3d5f88)" role="img" aria-label="Smiling builder in hard hat with arms crossed"></div>
  <div class="photo" style="left:63px;top:329px;width:287px;height:349px;background:linear-gradient(180deg,#e0a160,#8a6b55 45%,#3f3d3f)" role="img" aria-label="High-rise steel building under construction at dusk"></div>
  <h2><span>ABOUT</span> US</h2>
  <div class="copy">
    <p>Lorem ipsum odor amet, consectetuer adipiscing elit. Platea pulvinar lobortis fames, maecenas feugiat morbi venenatis.</p>
    <p>Lorem ipsum odor amet, consectetuer adipiscing elit. Nunc class maximus maximus integer vitae. Fames habitasse eu duis pretium id ultricies conubia. Morbi quisque rutrum volutpat vitae integer vehicula egestas. Vestibulum eget nostra blandit quam vitae donec.</p>
  </div>
  <div class="exp">
    <svg width="66" height="66" viewBox="0 0 66 66" fill="none" stroke="#1672c6" stroke-width="2.5"><rect x="4" y="8" width="44" height="34"/><path d="M10 18h14M10 26h10M10 34h12"/><circle cx="42" cy="42" r="12"/><path d="M51 51l10 10"/></svg>
    <div><b>15</b> years<br>Experience</div>
  </div>
  <div class="btn" style="left:660px;top:558px;width:157px;height:38px">Learn More</div>
</section>

<section class="products">
  <div class="sec-title" style="top:42px;color:#fff"><span>PRO</span>DUCTS</div>
  <div class="sec-text" style="top:110px">Lorem ipsum odor amet, consectetuer adipiscing elit. Platea pulvinar lobortis fames, maecenas feugiat</div>
  <div class="tab" style="left:345px;width:148px">INDUSTRIAL</div>
  <div class="tab active" style="left:527px;width:155px">RESIDENTIAL</div>
  <div class="tab" style="left:710px;width:156px">COMMERCIAL</div>
  <div class="abs" style="left:63px;top:248px;width:195px;height:148px;border:2px solid #fff;border-right:none;border-bottom:none"></div>
  <div class="pcard" style="left:88px">
    <div class="photo" style="inset:0;background:linear-gradient(150deg,#bcd2e3,#6f8ea8 50%,#2b3b4b)" role="img" aria-label="Curved steel roof truss lattice"></div>
    <div class="label light">Roof Trusses <svg width="24" height="16" viewBox="0 0 24 16"><path d="M1 8h20M14 1l7 7-7 7" fill="none" stroke="#1672c6" stroke-width="2"/></svg></div>
  </div>
  <div class="pcard" style="left:440px">
    <div class="photo" style="inset:0;background:linear-gradient(160deg,#8fb0d0,#c9c7b8 55%,#6c7380)" role="img" aria-label="Steel facade framing on a building"></div>
    <div class="label">Facade Framing <svg width="24" height="16" viewBox="0 0 24 16"><path d="M1 8h20M14 1l7 7-7 7" fill="none" stroke="#fff" stroke-width="2"/></svg></div>
  </div>
  <div class="pcard" style="left:792px">
    <div class="photo" style="inset:0;background:linear-gradient(170deg,#1e1e22,#6b4d3a 50%,#d48f4f 70%,#2a2a2e)" role="img" aria-label="Structural steel bridge girders at sunset"></div>
    <div class="label">Structural Steel <svg width="24" height="16" viewBox="0 0 24 16"><path d="M1 8h20M14 1l7 7-7 7" fill="none" stroke="#fff" stroke-width="2"/></svg></div>
  </div>
</section>

<section class="services">
  <div class="sec-title" style="top:48px"><span>SER</span>VICES</div>
  <div class="sec-text" style="top:115px">Lorem ipsum odor amet, consectetuer adipiscing elit. Platea pulvinar lobortis fames, maecenas feugiat</div>
  <div class="scard featured" style="left:63px"><h3>Industrial</h3><p>Lorem ipsum odor amet, consectetuer adipiscing elit</p><div class="btn">Learn More</div></div>
  <div class="scard" style="left:426px"><h3>Residential</h3><p>Lorem ipsum odor amet, consectetuer adipiscing elit</p><div class="btn">Learn More</div></div>
  <div class="scard" style="left:788px"><h3>Commercial</h3><p>Lorem ipsum odor amet, consectetuer adipiscing elit</p><div class="btn">Learn More</div></div>
  <div class="sicon light" style="left:188px"><svg width="46" height="46" viewBox="0 0 46 46" fill="none" stroke="#333" stroke-width="2"><path d="M4 42V22l10-6v6l10-6v6l10-6V8h6v34z"/><path d="M10 30h4M20 30h4M30 30h4"/></svg></div>
  <div class="sicon" style="left:550px"><svg width="40" height="46" viewBox="0 0 40 46" fill="none" stroke="#fff" stroke-width="2"><rect x="8" y="4" width="24" height="38"/><path d="M14 12h4M22 12h4M14 20h4M22 20h4M14 28h4M22 28h4"/></svg></div>
  <div class="sicon" style="left:913px"><svg width="46" height="46" viewBox="0 0 46 46" fill="none" stroke="#fff" stroke-width="2"><circle cx="15" cy="14" r="5"/><circle cx="31" cy="14" r="5"/><path d="M6 40V28a9 9 0 0118 0v12M22 40V28a9 9 0 0118 0v12"/></svg></div>
</section>

<section class="projects">
  <div class="sec-title" style="top:38px;color:#fff"><span>OUR</span> PROJECTS</div>
  <div class="sec-text" style="top:105px">Lorem ipsum odor amet, consectetuer adipiscing elit. Platea pulvinar lobortis fames, maecenas feugiat</div>
  <div class="jcard" style="left:63px">
    <div class="img" style="background:linear-gradient(170deg,#c8d6e2,#8f7a66 55%,#6a3b2a)" role="img" aria-label="Worker cutting steel beams in a workshop"></div>
    <div class="body blue"><h4>Carpenters Lane North Hastings</h4><svg class="arr" width="26" height="16" viewBox="0 0 26 16"><path d="M1 8h22M16 1l7 7-7 7" fill="none" stroke="#fff" stroke-width="2"/></svg><p>Lorem ipsum odor amet, consectetuer adipiscing elit. Platea pulvinar</p></div>
  </div>
  <div class="jcard" style="left:428px">
    <div class="img" style="background:linear-gradient(180deg,#c9d3c9,#5f7a44 55%,#3f4a34)" role="img" aria-label="Small timber cabin on a wheeled trailer"></div>
    <div class="body"><h4>Tiny Houses On Wheels</h4><svg class="arr" width="26" height="16" viewBox="0 0 26 16"><path d="M1 8h22M16 1l7 7-7 7" fill="none" stroke="#fff" stroke-width="2"/></svg><p>Lorem ipsum odor amet, consectetuer adipiscing elit. Platea pulvinar</p></div>
  </div>
  <div class="jcard" style="left:791px">
    <div class="img" style="background:linear-gradient(180deg,#b9c7d8,#5c6f88 50%,#2b3a4e)" role="img" aria-label="Looking through a steel truss bridge"></div>
    <div class="body"><h4>Structural Steel</h4><svg class="arr" width="26" height="16" viewBox="0 0 26 16"><path d="M1 8h22M16 1l7 7-7 7" fill="none" stroke="#fff" stroke-width="2"/></svg><p>Lorem ipsum odor amet, consectetuer adipiscing elit. Platea pulvinar</p></div>
  </div>
  <div class="btn" style="left:480px;top:685px;width:240px;height:40px">View All Project</div>
</section>

<section class="partners">
  <div class="sec-title" style="top:40px"><span>OUR</span> PARTNERS</div>
  <div class="sec-text" style="top:108px">Lorem ipsum odor amet, consectetuer adipiscing elit. Platea pulvinar lobortis fames, maecenas feugiat</div>
  <div class="pbox" style="left:63px"><div style="width:60px;height:60px;background:#333"></div></div>
  <div class="pbox" style="left:336px"><div style="width:70px;height:60px;background:#b08d3c"></div></div>
  <div class="pbox" style="left:607px"><div style="width:60px;height:60px;border-radius:50%;background:#1a5fae"></div></div>
  <div class="pbox" style="left:878px"><div style="width:60px;height:60px;background:#2d5f9a"></div></div>
</section>

<section class="split">
  <div class="certs">
    <h2><span>CERT</span>IFICATIONS</h2>
    <p>Lorem ipsum odor amet, consectetuer adipiscing elit.</p>
    <div class="abs" style="left:102px;top:164px;width:285px;height:185px;background:linear-gradient(90deg,#c0262c 0 22%,#f4f1ec 22%)" role="img" aria-label="QSB quality certificate"></div>
    <div class="round" style="left:24px;top:219px"><svg width="14" height="14" viewBox="0 0 14 14"><path d="M9 2L4 7l5 5" fill="none" stroke="#fff" stroke-width="2"/></svg></div>
    <div class="round" style="left:427px;top:219px"><svg width="14" height="14" viewBox="0 0 14 14"><path d="M5 2l5 5-5 5" fill="none" stroke="#fff" stroke-width="2"/></svg></div>
    <div class="dot" style="left:208px"></div>
    <div class="dot" style="left:235px;background:var(--blue)"></div>
    <div class="dot" style="left:262px"></div>
  </div>
  <div class="contact">
    <h2><span>CON</span>TACT US</h2>
    <div class="field" style="left:55px;top:90px;width:232px;height:39px">First Name</div>
    <div class="field" style="left:292px;top:90px;width:222px;height:39px">Last Name</div>
    <div class="field" style="left:55px;top:142px;width:459px;height:39px">Email Address</div>
    <div class="field" style="left:55px;top:194px;width:459px;height:39px">Phone</div>
    <div class="field" style="left:55px;top:246px;width:459px;height:85px">message</div>
    <div class="submit">SUBMIT</div>
  </div>
</section>

<footer class="site-footer">
  <div class="foot-brand"><i></i><b>TARNWICK</b></div>
  <ul class="foot-links"><li class="active">HOME</li><li>ABOUT</li><li>SERVICES</li><li>PRODUCTS</li><li>CONTACT</li></ul>
  <div class="social" style="left:964px" aria-label="Photo sharing profile"></div>
  <div class="social" style="left:1014px" aria-label="Social network page"></div>
  <div class="social" style="left:1060px" aria-label="Microblog profile"></div>
  <div class="foot-rule"></div>
  <div class="copyright">© 2024 All Rights Reserved | Tarnwick</div>
</footer>

</body>
</html>
```